TriVex Business Card Design - double sided -plumbing local plumbing company

We have a Plumbing company where the design was create through Sketch Hive. We would now like a business card designed as well. We want it to be in the colour version of the logo.

Details below for the card.

Phone Number: 0438 615 247
Email: info@trivexplumbing.example.au
Website: https://trivexplumbing.example.au
We really want a sophisticated design that stand out from the other- informative and timeless.

Target Market(s)

local Canberra market

Industry/Entity Type

Plumbing, gas fitting, hot water

Contact Information for Business Card

Phone number, email, logo and "Supplying all your heating, cooling and hot water needs"

Requirements
Must have
• bust be colourful, must also be though about it being printed on a magnet. must Vex with the logo - I dont want the logo and information chucked onto a white canvas I would prefer it to be smooth and look purposeful

```html
<!DOCTYPE html>
<html lang="en">
<head>
<meta charset="utf-8">
<title>TriVex Plumbing – Business Card</title>
<link rel="stylesheet" href="https://fonts.googleapis.com/css2?family=Arimo:wght@400;700&display=swap">
<style>
  :root {
    --page-bg: #e4e5e7;
    --card-bg: #ffffff;
    --card-shade: #eeeeee;
    --brand-blue: #1b9bd7;
    --brand-orange: #eda23a;
    --ink: #3a3d42;
    --ink-dark: #1f2a3a;
    --rule: #1f2f48;
  }
  * { margin: 0; padding: 0; box-sizing: border-box; }
  html, body {
    width: 1200px; height: 900px; overflow: hidden;
    background: var(--page-bg);
    font-family: "Arimo", Arial, sans-serif;
    color: var(--ink);
  }
  .sheet {
    position: relative; width: 1200px; height: 900px;
    display: flex; flex-direction: column; align-items: center;
    justify-content: center; gap: 44px;
  }
  .card {
    position: relative; width: 700px; height: 400px;
    border-radius: 34px;
    background: linear-gradient(135deg, var(--card-bg) 0%, var(--card-bg) 55%, var(--card-shade) 100%);
    box-shadow: 0 14px 30px rgba(0,0,0,.18);
    overflow: hidden;
  }
  .brand {
    position: absolute; display: flex; align-items: center; gap: 12px;
  }
  .brand-name {
    font-weight: 700; color: var(--brand-blue); letter-spacing: 1px; line-height: 1;
  }
  .brand-dot {
    border-radius: 50%; background: var(--brand-orange);
  }
  .brand-rule {
    position: absolute; height: 2px; background: var(--rule);
  }
  .tagline { position: absolute; font-size: 17px; color: var(--ink); letter-spacing: .3px; }

  /* back side */
  .card--back .brand { left: 40px; top: 118px; }
  .card--back .brand-name { font-size: 78px; }
  .card--back .brand-dot { width: 40px; height: 40px; }
  .card--back .brand-rule { left: 40px; top: 212px; width: 340px; }
  .card--back .tagline { left: 40px; top: 224px; font-size: 15px; }
  .website { position: absolute; left: 40px; top: 250px; font-size: 16px; color: var(--ink-dark); }

  .services { position: absolute; left: 440px; top: 116px; }
  .services-title {
    font-size: 17px; font-weight: 700; color: var(--brand-blue);
    margin-bottom: 8px; letter-spacing: .3px;
  }
  .services-list { list-style: none; }
  .services-list li {
    display: flex; align-items: center; gap: 10px;
    font-size: 16px; line-height: 27px; color: var(--ink);
  }
  .services-list li::before {
    content: ""; width: 7px; height: 7px; border-radius: 50%;
    background: var(--brand-blue); flex: none;
  }

  /* front side */
  .card--front .brand { left: 40px; top: 92px; }
  .card--front .brand-name { font-size: 104px; }
  .card--front .brand-dot { width: 52px; height: 52px; }
  .card--front .brand-rule { left: 40px; top: 214px; width: 470px; }
  .card--front .tagline { left: 40px; top: 228px; }

  .contact { position: absolute; left: 400px; top: 292px; }
  .contact-row {
    display: flex; align-items: center; gap: 10px;
    font-size: 18px; line-height: 32px; color: var(--ink);
  }
  .contact-row svg { width: 20px; height: 20px; flex: none; }
</style>
</head>
<body>
<main class="sheet">

  <section class="card card--back" aria-label="Business card, back">
    <div class="brand">
      <span class="brand-name">TriVex</span>
      <span class="brand-dot"></span>
    </div>
    <div class="brand-rule"></div>
    <p class="tagline">We cover all of the ACT and surrounding areas.</p>
    <p class="website">trivexplumbing.example.au</p>

    <div class="services">
      <h2 class="services-title">OUR SERVICE</h2>
      <ul class="services-list">
        <li>Heat Pump Hot Water</li>
        <li>Home Air Conditioning</li>
        <li>General Plumbing</li>
        <li>Renovations</li>
        <li>Testing &amp; Repairs</li>
      </ul>
    </div>
  </section>

  <section class="card card--front" aria-label="Business card, front">
    <div class="brand">
      <span class="brand-name">TriVex</span>
      <span class="brand-dot"></span>
    </div>
    <div class="brand-rule"></div>
    <p class="tagline">Supplying all your heating, cooling and hot water needs</p>

    <div class="contact">
      <p class="contact-row">
        <svg viewBox="0 0 24 24" aria-hidden="true"><path fill="#1b9bd7" d="M6.6 10.8a15.1 15.1 0 0 0 6.6 6.6l2.2-2.2c.3-.3.7-.4 1-.2 1.1.4 2.3.6 3.6.6.6 0 1 .4 1 1V20c0 .6-.4 1-1 1C10.6 21 3 13.4 3 4c0-.6.4-1 1-1h3.5c.6 0 1 .4 1 1 0 1.3.2 2.5.6 3.6.1.3 0 .7-.2 1z"/></svg>
        0438 615 247
      </p>
      <p class="contact-row">
        <svg viewBox="0 0 24 24" aria-hidden="true"><rect x="2" y="5" width="20" height="14" rx="1.5" fill="#1b9bd7"/><path d="M3 6.5l9 6.5 9-6.5" fill="none" stroke="#fff" stroke-width="1.6"/></svg>
        info@trivexplumbing.example.au
      </p>
      <p class="contact-row">
        <svg viewBox="0 0 24 24" aria-hidden="true"><circle cx="12" cy="12" r="9" fill="none" stroke="#1b9bd7" stroke-width="2"/><path d="M3 12h18M12 3c3 3 3 15 0 18M12 3c-3 3-3 15 0 18" fill="none" stroke="#1b9bd7" stroke-width="1.6"/></svg>
        trivexplumbing.example.au
      </p>
    </div>
  </section>

</main>
</body>
</html>
```